BKT Business Card

Business card design for a handyman company. Want to portray a professional image and stay away from the "Mom & Pops" image that is normally associated with handyman companies.

```html
<!DOCTYPE html>
<html lang="en">
<head>
<meta charset="utf-8">
<title>BKT Business Card</title>
<link rel="stylesheet" href="https://fonts.googleapis.com/css2?family=Exo+2:wght@400;500;700;800&display=swap">
<style>
  :root {
    --backdrop: #5b3c27;
    --card-white: #ffffff;
    --card-mist: #e9edf2;
    --navy: #132a4f;
    --navy-deep: #0f2244;
    --ink-light: #e6ecf5;
    --pill: #dde3ea;
  }
  * { margin: 0; padding: 0; box-sizing: border-box; }
  html, body {
    width: 1200px;
    height: 867px;
    overflow: hidden;
    background: var(--backdrop);
    font-family: "Exo 2", sans-serif;
  }
  .card {
    position: absolute;
    left: 120px;
    top: 159px;
    width: 960px;
    height: 549px;
    background: linear-gradient(180deg, var(--card-white) 0%, var(--card-mist) 56%);
    box-shadow: 0 14px 40px rgba(0,0,0,0.35);
    overflow: hidden;
  }
  .brand {
    position: absolute;
    top: 70px;
    left: 0;
    width: 100%;
    text-align: center;
    padding-left: 90px;
    font-weight: 800;
    font-size: 76px;
    color: var(--navy);
    letter-spacing: 1px;
    line-height: 1;
  }
  .tagline {
    position: absolute;
    top: 262px;
    left: 0;
    width: 100%;
    text-align: center;
    padding-left: 110px;
    font-weight: 500;
    font-size: 24px;
    letter-spacing: 3.5px;
    color: var(--navy);
  }
  .band {
    position: absolute;
    left: 0;
    top: 312px;
    width: 100%;
    height: 237px;
    background: linear-gradient(180deg, var(--navy) 0%, var(--navy-deep) 100%);
    color: var(--ink-light);
  }
  .contact {
    position: absolute;
    left: 60px;
    top: 32px;
    list-style: none;
    font-size: 20px;
    line-height: 34px;
    letter-spacing: 0.5px;
  }
  .address {
    position: absolute;
    left: 60px;
    top: 172px;
    font-size: 20px;
    letter-spacing: 0.5px;
  }
  .services {
    position: absolute;
    left: 575px;
    top: 24px;
    list-style: none;
    font-size: 18px;
    line-height: 27px;
    letter-spacing: 0.4px;
  }
  .services li {
    display: flex;
    align-items: center;
    gap: 14px;
  }
  .services li::before {
    content: "";
    width: 13px;
    height: 13px;
    border-radius: 50%;
    background: var(--card-white);
  }
  .website {
    position: absolute;
    right: 22px;
    top: 140px;
    height: 38px;
    padding: 0 26px;
    display: flex;
    align-items: center;
    border-radius: 19px 0 0 19px;
    background: var(--pill);
    color: var(--navy);
    font-size: 20px;
    letter-spacing: 0.6px;
  }
</style>
</head>
<body>
  <section class="card" aria-label="BKT Maintenance business card">
    <h1 class="brand">BKT Maintenance</h1>
    <p class="tagline">RESIDENTIAL &amp; COMMERCIAL SERVICES</p>
    <div class="band">
      <ul class="contact">
        <li>P: (555) 014-7200</li>
        <li>F: (555) 014-7291</li>
        <li>E: info@BKTMaintenance.com</li>
      </ul>
      <p class="address">2750 W Prairie Ln, Salina, Ks 67401</p>
      <ul class="services">
        <li>Home Repairs</li>
        <li>Handyman Services</li>
        <li>Drain Cleaning</li>
        <li>Carpet Cleaning</li>
      </ul>
      <p class="website">www.BKTMaintenance.com</p>
    </div>
  </section>
</body>
</html>
```